Website Layout for PanFolio

PanFolio is a company that will be dedicated (for now) to publishing recipes with the nutrition facts. Run by a nutritionist. In the future there may be a mobile app.

We need layout for 3 of the pages of the website. NO PROGRAMMING, only layout and graphic design. Not very complicated.

--Please view the details in the attached document--
We want a layout design for the pages: P.01, P.02 and P.03

Logo is also attached. Please don't hesitate if you want to modify the logo to fit your idea. The design should be clean, visually attractive and refreshing to look at. It should be sleek and a feel of technology, yet also natural and culinary.

Some examples to get ideas:

http://www.marlowhearthtales.com/
http://www.tavelbrunefare.org/site/
http://thecobaltladle.com/products/dice-deck
Updates

Project Deadline Extended
Reason: I extend the deadline for this week to allow you space for work on the observations made to your design and to provide the P.02 and P.03 designs. We greatly appreciate your hard work and are thrilled with your ideas.

Target Market(s)

Young people that live alone or want to optimize their cooking.
Young, modern housewives with a smartphone.

Industry/Entity Type

Nutrition

Requirements
Must have
• --Please view the details in the attached document--
NO PROGRAMMING. Only layout and graphic design.

```html
<!DOCTYPE html>
<html lang="en">
<head>
<meta charset="utf-8">
<title>PanFolio — Recipes with Nutrition Facts</title>
<link rel="stylesheet" href="https://fonts.googleapis.com/css2?family=Open+Sans:wght@400;600&family=Roboto+Condensed:wght@400&family=Amatic+SC:wght@700&display=swap">
<style>
  :root {
    --ink: #333333;
    --ink-soft: #555555;
    --green: #6aa832;
    --green-dark: #4f8a22;
    --orange: #f7941d;
    --olive: #d4c56c;
    --olive-dark: #b6a64c;
    --red: #d9352b;
    --band: rgba(40, 40, 40, 0.72);
    --line: #e3e3e3;
    --footer-bg: #f4f4f4;
    --white: #ffffff;
  }
  * { box-sizing: border-box; margin: 0; padding: 0; }
  html, body { width: 1200px; height: 938px; overflow: hidden; }
  body {
    position: relative;
    background: var(--white);
    font-family: "Open Sans", Arial, sans-serif;
    color: var(--ink);
  }

  .social { position: absolute; left: 43px; top: 46px; display: flex; gap: 6px; }
  .social a { width: 26px; height: 26px; border-radius: 4px; display: block; }
  .social .s1 { background: var(--orange); }
  .social .s2 { background: var(--red); }
  .social .s3 { background: var(--green); }

  .brand { position: absolute; left: 466px; top: 22px; display: flex; align-items: center; gap: 14px; }
  .brand-mark { width: 80px; height: 80px; background: var(--orange); border-radius: 6px; }
  .brand-name { font-size: 40px; font-weight: 600; color: var(--ink-soft); letter-spacing: -0.5px; }

  .account { position: absolute; right: 42px; top: 40px; display: flex; gap: 10px; }
  .btn {
    display: inline-flex; align-items: center; justify-content: center;
    height: 31px; border-radius: 3px; font-size: 14px; color: var(--ink);
    text-decoration: none;
  }
  .btn-signin { width: 84px; background: linear-gradient(#dccd78, var(--olive-dark)); }
  .btn-register { width: 84px; background: linear-gradient(#fba43a, var(--orange)); color: var(--white); }

  .search { position: absolute; left: 323px; top: 145px; width: 553px; height: 40px; display: flex; }
  .search-field {
    flex: 1; border: 1px solid #c9c9c9; border-right: 0; border-radius: 3px 0 0 3px;
    font: 14px "Open Sans", Arial, sans-serif; color: #777; padding-left: 12px;
    display: flex; align-items: center;
  }
  .search-btn {
    width: 41px; background: linear-gradient(#7bbb3c, var(--green-dark));
    border-radius: 0 3px 3px 0; display: flex; align-items: center; justify-content: center;
  }

  .categories {
    position: absolute; left: 42px; top: 214px;
    display: grid; grid-template-columns: repeat(4, 272px); grid-auto-rows: 216px;
    column-gap: 9px; row-gap: 10px;
  }
  .tile { position: relative; border-radius: 3px; overflow: hidden; box-shadow: 0 0 3px rgba(0,0,0,0.18); }
  .tile-photo { position: absolute; inset: 0; }
  .tile-zoom {
    position: absolute; left: 108px; top: 80px; width: 56px; height: 56px; border-radius: 50%;
    background: rgba(255,255,255,0.35); display: flex; align-items: center; justify-content: center;
  }
  .tile-label {
    position: absolute; left: 0; right: 0; bottom: 0; height: 40px; background: var(--band);
    color: var(--white); font-family: "Amatic SC", "Trebuchet MS", cursive; font-size: 24px;
    padding-left: 12px; line-height: 40px;
  }

  .p1 { background: radial-gradient(circle at 50% 60%, #b07a45, #e9e4dd 70%); }
  .p2 { background: radial-gradient(circle at 50% 45%, #d8602a, #ecd9a5 55%, #f4f1ea 75%); }
  .p3 { background: radial-gradient(circle at 55% 35%, #e5c77a, #a9c0d8 60%, #dfe7ef); }
  .p4 { background: linear-gradient(120deg, #cfe2a8, #5a3a22 55%, #f2d400); }
  .p5 { background: radial-gradient(circle at 40% 40%, #9b3a1e, #c86a3a 55%, #f0a23a); }
  .p6 { background: linear-gradient(160deg, #4d4a40, #2d2c28); }
  .p7 { background: radial-gradient(circle at 55% 55%, #e7a12f, #f5efe6 45%, #d27b4a); }
  .p8 { background: linear-gradient(150deg, #f1ebe2, #7aa246 50%, #c8342a); }

  .tile-detail { position: absolute; inset: 0; background: rgba(20,20,20,0.62); padding: 10px 14px; color: var(--white); }
  .tile-detail h3 {
    font-family: "Amatic SC", "Trebuchet MS", cursive; font-weight: 700; font-size: 24px;
    border-bottom: 1px solid rgba(255,255,255,0.6); padding-bottom: 2px; margin-bottom: 10px;
  }
  .facts { list-style: none; background: rgba(20,20,20,0.5); }
  .facts li { font-size: 15px; height: 36px; line-height: 36px; padding-left: 8px; border-bottom: 1px solid rgba(255,255,255,0.12); }
  .btn-read {
    margin-top: 8px; width: 107px; height: 33px; background: linear-gradient(#78b73c, var(--green-dark));
    color: var(--white); font-size: 15px; border-radius: 2px;
  }

  .intro { position: absolute; top: 683px; left: 0; width: 1200px; text-align: center; font-size: 15px; line-height: 24px; color: var(--ink); }

  .main-nav { position: absolute; top: 767px; left: 0; width: 1200px; display: flex; justify-content: center; }
  .main-nav a {
    display: flex; align-items: center; gap: 8px; height: 34px; padding: 0 18px;
    font-family: "Roboto Condensed", Arial, sans-serif; font-size: 19px; color: var(--ink); text-decoration: none;
  }
  .main-nav a + a { border-left: 1px solid #bdbdbd; }

  .site-footer {
    position: absolute; left: 0; top: 822px; width: 1200px; height: 116px;
    background: var(--footer-bg); border-top: 1px solid var(--line);
  }
  .footer-mark { position: absolute; left: 46px; top: 18px; width: 76px; height: 78px; background: var(--orange); border-radius: 6px; }
  .copyright { position: absolute; left: 137px; top: 54px; font-size: 14px; color: var(--ink-soft); }
  .contact { position: absolute; right: 42px; top: 53px; text-align: right; font-size: 14px; line-height: 21px; color: var(--ink); }
</style>
</head>
<body>

<header>
  <nav class="social" aria-label="Social links">
    <a class="s1" href="#" aria-label="Social network one"></a>
    <a class="s2" href="#" aria-label="Social network two"></a>
    <a class="s3" href="#" aria-label="Social network three"></a>
  </nav>

  <div class="brand">
    <span class="brand-mark"></span>
    <span class="brand-name">PanFolio</span>
  </div>

  <div class="account">
    <a class="btn btn-signin" href="#">Sign In</a>
    <a class="btn btn-register" href="#">Register</a>
  </div>

  <form class="search" role="search">
    <div class="search-field">Enter Your Searh Items</div>
    <div class="search-btn">
      <svg width="20" height="20" viewBox="0 0 20 20"><circle cx="8" cy="8" r="6" fill="none" stroke="#fff" stroke-width="2.6"/><line x1="12.5" y1="12.5" x2="18" y2="18" stroke="#fff" stroke-width="3" stroke-linecap="round"/></svg>
    </div>
  </form>
</header>

<main>
  <section class="categories">
    <article class="tile">
      <div class="tile-photo p1" role="img" aria-label="Chocolate chip cookies with a glass of milk"></div>
      <div class="tile-zoom"><svg width="26" height="26" viewBox="0 0 20 20"><circle cx="8" cy="8" r="6" fill="none" stroke="#fff" stroke-width="2.4"/><line x1="12.5" y1="12.5" x2="18" y2="18" stroke="#fff" stroke-width="3" stroke-linecap="round"/></svg></div>
      <h3 class="tile-label">Category One</h3>
    </article>
    <article class="tile">
      <div class="tile-photo p2" role="img" aria-label="Bowl of vegetable soup with carrots"></div>
      <div class="tile-zoom"><svg width="26" height="26" viewBox="0 0 20 20"><circle cx="8" cy="8" r="6" fill="none" stroke="#fff" stroke-width="2.4"/><line x1="12.5" y1="12.5" x2="18" y2="18" stroke="#fff" stroke-width="3" stroke-linecap="round"/></svg></div>
      <h3 class="tile-label">Category Two</h3>
    </article>
    <article class="tile">
      <div class="tile-photo p3" role="img" aria-label="Noodle soup in a white bowl"></div>
      <div class="tile-zoom"><svg width="26" height="26" viewBox="0 0 20 20"><circle cx="8" cy="8" r="6" fill="none" stroke="#fff" stroke-width="2.4"/><line x1="12.5" y1="12.5" x2="18" y2="18" stroke="#fff" stroke-width="3" stroke-linecap="round"/></svg></div>
      <h3 class="tile-label">Category Three</h3>
    </article>
    <article class="tile">
      <div class="tile-photo p4" role="img" aria-label="Grilled skewers with cucumber on a plate"></div>
      <div class="tile-zoom"><svg width="26" height="26" viewBox="0 0 20 20"><circle cx="8" cy="8" r="6" fill="none" stroke="#fff" stroke-width="2.4"/><line x1="12.5" y1="12.5" x2="18" y2="18" stroke="#fff" stroke-width="3" stroke-linecap="round"/></svg></div>
      <h3 class="tile-label">Category Four</h3>
    </article>
    <article class="tile">
      <div class="tile-photo p5" role="img" aria-label="Glazed roast ham with orange slices"></div>
      <div class="tile-zoom"><svg width="26" height="26" viewBox="0 0 20 20"><circle cx="8" cy="8" r="6" fill="none" stroke="#fff" stroke-width="2.4"/><line x1="12.5" y1="12.5" x2="18" y2="18" stroke="#fff" stroke-width="3" stroke-linecap="round"/></svg></div>
      <h3 class="tile-label">Category Five</h3>
    </article>
    <article class="tile">
      <div class="tile-photo p6" role="img" aria-label="Plated dish behind a dark overlay"></div>
      <div class="tile-detail">
        <h3>Category Six</h3>
        <ul class="facts">
          <li>Calories: 230 Kcal</li>
          <li>Fat: 20g</li>
          <li>Complexity of recipe: 30 Mins</li>
        </ul>
        <a class="btn btn-read" href="#">Read More</a>
      </div>
    </article>
    <article class="tile">
      <div class="tile-photo p7" role="img" aria-label="Cup of creamy pumpkin soup"></div>
      <div class="tile-zoom"><svg width="26" height="26" viewBox="0 0 20 20"><circle cx="8" cy="8" r="6" fill="none" stroke="#fff" stroke-width="2.4"/><line x1="12.5" y1="12.5" x2="18" y2="18" stroke="#fff" stroke-width="3" stroke-linecap="round"/></svg></div>
      <h3 class="tile-label">Category Seven</h3>
    </article>
    <article class="tile">
      <div class="tile-photo p8" role="img" aria-label="Buffet platter with salads and vegetables"></div>
      <div class="tile-zoom"><svg width="26" height="26" viewBox="0 0 20 20"><circle cx="8" cy="8" r="6" fill="none" stroke="#fff" stroke-width="2.4"/><line x1="12.5" y1="12.5" x2="18" y2="18" stroke="#fff" stroke-width="3" stroke-linecap="round"/></svg></div>
      <h3 class="tile-label">Category Eight</h3>
    </article>
  </section>

  <p class="intro">Lorem ipsum dolor sit amet, consectetur adipiscing elit. Ut sit amet metus ut lorem pharetra venenatis fermentum at nibh.<br>Nulla aliquet diam eu turpis convallis sit amet malesuada mi ultrices. In in velit massa, vitae condimentum leo.</p>

  <nav class="main-nav" aria-label="Main">
    <a href="#"><svg width="20" height="18" viewBox="0 0 20 18"><path d="M10 1 L19 9 H16 V17 H12 V12 H8 V17 H4 V9 H1 Z" fill="#6aa832"/></svg>Home</a>
    <a href="#"><svg width="16" height="20" viewBox="0 0 16 20"><rect x="2" y="1" width="12" height="18" rx="1" fill="#d9352b"/><rect x="5" y="4" width="6" height="2" fill="#fff"/></svg>About</a>
    <a href="#"><svg width="24" height="18" viewBox="0 0 24 18"><rect x="1" y="2" width="22" height="14" rx="2" fill="#f7941d"/><path d="M2 3 L12 10 L22 3" fill="none" stroke="#fff" stroke-width="2"/></svg>Contact Us</a>
  </nav>
</main>

<footer class="site-footer">
  <span class="footer-mark"></span>
  <p class="copyright">© 2014 by PanFolio. All Rights Reserved</p>
  <address class="contact" style="font-style:normal">hello@panfolio-recipes.com<br>+1 555 014 7720</address>
</footer>

</body>
</html>
```